Managed Service Provider email

We need an email designed that advertises our Managed Services product. We have been in business 28 years. Managed Services includes proactive ticketing, Help desk support, server and workstation monitoring, data backup monitoring, spam protection, regular reports, Deskflow 240, telecom services, ISP management, vendor management and more.

Target Market(s)

Business owners, decision makers, IT, CTO

Industry/Entity Type

Information Technology

Colors

Designer to choose colors to be used in the design.

Requirements
Must have
• Bullet points with included services. Mention of 28 years in business.
Nice to have
• We'd love our designer to read up on what an MSP (Managed Service Provider) does and use that information to find/create content for our email project.
Should not have
• A picture of a computer with a thermometer in its mouth.

```html
<!DOCTYPE html>
<html lang="en">
<head>
<meta charset="utf-8">
<title>Vantor Managed Services Email</title>
<link href="https://fonts.googleapis.com/css2?family=Montserrat:wght@400;600;700;800&family=Raleway:wght@300;400;500;700&display=swap" rel="stylesheet">
<style>
  :root {
    --ink: #2b2b2b;
    --black: #000;
    --white: #fff;
    --orange: #ff6b45;
    --blue-hero: #2f4db8;
    --blue-deep: #1f3591;
    --blue-cta: #2a8fe6;
    --panel: #2c2c30;
    --card: #1b1c22;
    --navy-brand: #22305a;
  }
  * { box-sizing: border-box; margin: 0; padding: 0; }
  html, body { width: 1200px; height: 1200px; overflow: hidden; background: var(--black); }
  body { position: relative; font-family: "Raleway", sans-serif; color: var(--ink); }

  /* Intro email (light) */
  .email-intro {
    position: absolute; left: 70px; top: 30px; width: 460px; height: 1130px;
    background: var(--white);
  }
  .brand-bar { height: 80px; display: flex; align-items: center; justify-content: center; }
  .brand-name { font-family: "Montserrat", sans-serif; font-weight: 800; font-size: 30px; letter-spacing: 1px; color: var(--navy-brand); }
  .hero {
    height: 420px; background: linear-gradient(180deg, var(--blue-hero), var(--blue-deep));
    padding-top: 20px; text-align: center; display: flex; flex-direction: column;
  }
  .hero-lead { font-family: "Montserrat", sans-serif; font-weight: 700; font-size: 16px; line-height: 21px; color: var(--white); }
  .hero-title {
    margin: 18px auto 0; width: 290px; background: var(--orange); padding: 9px 0 9px 30px;
    text-align: left; position: relative;
  }
  .hero-title::before { content: ""; position: absolute; left: 18px; top: 11px; bottom: 11px; width: 3px; background: var(--white); }
  .hero-title span { display: block; font-family: "Montserrat", sans-serif; font-weight: 800; font-size: 28px; letter-spacing: 6px; line-height: 32px; color: var(--white); }
  .hero-collage {
    margin: 22px 0 0; flex: 1;
    background: linear-gradient(135deg, #3b3f4a 0%, #6a7488 35%, #2e55c8 60%, #1b2a52 100%);
  }
  .intro-body { padding: 26px 44px 0; text-align: center; font-size: 12.5px; line-height: 20px; color: #444; }
  .intro-body p + p { margin-top: 10px; }
  .intro-body strong { font-weight: 700; color: #222; }
  .services-heading { margin-top: 16px; font-family: "Montserrat", sans-serif; font-weight: 700; font-size: 13px; color: var(--navy-brand); }
  .services-list {
    margin-top: 8px; text-align: left; columns: 2; column-gap: 20px;
    list-style: none; font-size: 12.5px; line-height: 21px; color: #444;
  }
  .services-list li { padding-left: 14px; position: relative; break-inside: avoid; }
  .services-list li::before { content: ""; position: absolute; left: 0; top: 8px; width: 6px; height: 6px; background: var(--orange); }
  .btn-learn {
    display: inline-block; margin-top: 24px; background: var(--orange); color: var(--white);
    font-family: "Montserrat", sans-serif; font-weight: 700; font-size: 12px; letter-spacing: 1px;
    padding: 15px 40px;
  }

  /* Services email (dark) */
  .email-services {
    position: absolute; left: 580px; top: 30px; width: 560px; height: 730px;
    background: radial-gradient(circle at 50% 30%, #37373c, var(--panel) 70%);
    text-align: center; color: var(--white);
  }
  .email-services .brand-name { color: var(--white); display: block; padding-top: 44px; font-size: 28px; }
  .services-title { margin-top: 30px; font-weight: 400; font-size: 30px; letter-spacing: 4px; line-height: 34px; }
  .services-sub { margin: 18px auto 0; width: 340px; font-weight: 300; font-size: 15px; line-height: 25px; color: #d4d4d8; }
  .cards { margin: 22px 18px 0; text-align: left; }
  .card-row { display: flex; gap: 16px; }
  .card-col { flex: 1; }
  .card-head, .card-wide {
    background: var(--card); border-radius: 6px; display: flex; align-items: center; height: 42px; padding: 0 10px;
  }
  .tag { background: var(--orange); color: var(--white); font-family: "Montserrat", sans-serif; font-weight: 700; font-size: 11px; padding: 2px 7px; border-radius: 3px; }
  .card-name { font-family: "Montserrat", sans-serif; font-weight: 700; font-size: 19px; color: #c8c8cc; margin-left: 14px; }
  .card-list { list-style: none; padding: 10px 16px 12px; font-weight: 300; font-size: 16px; line-height: 23px; color: #c8c8cc; }
  .card-wide { margin-top: 10px; height: 44px; }
  .card-wide .card-name { margin-left: 10px; }
  .card-detail { margin-left: auto; font-size: 16px; color: #c8c8cc; padding-right: 4px; }
  .card-detail.fixed { margin-left: 112px; }
  .btn-help {
    display: inline-block; margin-top: 36px; background: var(--blue-cta); color: var(--white);
    font-family: "Montserrat", sans-serif; font-weight: 700; font-size: 13px; padding: 20px 58px;
  }
  .partners { display: flex; justify-content: center; gap: 34px; margin-top: 36px; }
  .partner-badge { width: 70px; height: 26px; border-radius: 4px; background: #4a4a50; }

  /* Footer */
  .footer { position: absolute; left: 580px; top: 800px; width: 560px; text-align: center; color: #9a9aa0; }
  .footer-label { font-family: "Montserrat", sans-serif; font-weight: 700; font-size: 11px; letter-spacing: 1px; color: #cfcfd3; }
  .social { display: flex; justify-content: center; gap: 14px; margin-top: 18px; }
  .social span { width: 40px; height: 40px; border-radius: 4px; background: #5a5a5f; }
  .footer-links { margin-top: 28px; font-size: 12px; letter-spacing: .5px; color: #c47a5c; }
  .footer-links i { font-style: normal; color: #666; margin: 0 12px; }
  .footer-company { margin-top: 30px; font-weight: 700; font-size: 12px; color: #cfcfd3; }
  .footer-address { margin-top: 10px; font-size: 12px; line-height: 22px; color: #9a9aa0; }
</style>
</head>
<body>

  <section class="email-intro">
    <header class="brand-bar"><span class="brand-name">Vantor</span></header>
    <div class="hero">
      <p class="hero-lead">See how you can improve operations<br>and cut IT expenses with our</p>
      <h1 class="hero-title"><span>MANAGED</span><span>SERVICES</span></h1>
      <div class="hero-collage" role="img" aria-label="Collage of photos: a businessman using a tablet, network cabling, a laptop keyboard, social apps on a phone and a server console"></div>
    </div>
    <div class="intro-body">
      <p>Looking for ways to make your business more profitable &amp; trim overhead expenses? Group together your IT needs and allow an outsourcing IT company to have a full scope of your business.</p>
      <p><strong>Vantor Network Service</strong> is a <em>Managed Service Provider</em> (MSP) - a company that takes care of your IT infrastructure, usually based on a subscription model. A MSP will proactively maintain your network and systems in order to detect and fix any problem that will affect your business. <strong>28 years in business</strong> and counting.</p>
      <p class="services-heading">Our Managed Services include:</p>
      <ul class="services-list">
        <li>Proactive ticketing</li>
        <li>Help desk support</li>
        <li>Server monitoring</li>
        <li>Workstation monitoring</li>
        <li>Data backup monitoring</li>
        <li>Spam protection</li>
        <li>Regular reports</li>
        <li>Deskflow 240</li>
        <li>Telecom services</li>
        <li>ISP management</li>
        <li>Vendor management</li>
        <li>And more</li>
      </ul>
      <a class="btn-learn">LEARN MORE</a>
    </div>
  </section>

  <section class="email-services">
    <span class="brand-name">Vantor</span>
    <h2 class="services-title">YOUR LOCAL, FRIENDLY<br>IT DEPARTMENT</h2>
    <p class="services-sub">Computers, Servers, Phones, Fiber, Cabling, Wireless, we can handle all of your Information Technology needs.</p>
    <div class="cards">
      <div class="card-row">
        <div class="card-col">
          <div class="card-head"><span class="tag">MSP</span><span class="card-name">MANAGED IT</span></div>
          <ul class="card-list"><li>Network Management</li><li>Workstation Monitoring</li><li>Server monitoring</li></ul>
        </div>
        <div class="card-col">
          <div class="card-head"><span class="tag">MSP</span><span class="card-name">CLOUD SERVICES</span></div>
          <ul class="card-list"><li>Deskflow 240</li><li>Cloud Servers</li><li>Cloud app. implementation</li></ul>
        </div>
      </div>
      <div class="card-wide"><span class="tag">MSP</span><span class="card-name">BUSINESS PHONES</span><span class="card-detail">Systems / Mobile / SIP Trunking</span></div>
      <div class="card-wide"><span class="tag">MSP</span><span class="card-name">CABLING</span><span class="card-detail fixed">Structured Cabling / Fiber</span></div>
    </div>
    <a class="btn-help">Need IT Help? Let us know</a>
    <div class="partners">
      <span class="partner-badge"></span><span class="partner-badge"></span><span class="partner-badge"></span><span class="partner-badge"></span><span class="partner-badge"></span>
    </div>
  </section>

  <footer class="footer">
    <p class="footer-label">FOLLOW US ON</p>
    <div class="social"><span></span><span></span></div>
    <p class="footer-links">CUSTOMER LOGIN<i>|</i>SUPPORT SESSION<i>|</i>UNSUSCRIBE</p>
    <p class="footer-company">Vantor Network Services</p>
    <p class="footer-address">418 North Cedar Avenue<br>Fairview, ST, 00000 - United States</p>
  </footer>

</body>
</html>
```